Redesign our business card for more impact

We want to completely replace the back design of our card, and refresh or even change the front entirely. We are happy with our black K4 logo and do not want to change it.
Our company address changed too. It is now 2307 Larkmoor, Irvine, CA 92741
Updates

It was reported by Art Harbor email today that the uploaded files didnt upload. I am trying again.

Target Market(s)

Architects and Building Owners (People making multi-million dollar decisions)

Industry/Entity Type

Consulting Engineering

Contact Information for Business Card

Contact info on the front. "wallpaper" design on back with tag line on the back "Engineering Your Future"

Font styles to use
Sans Serif

Requirements
Must have
• A vivid, modern, impactful ...but tasteful back of card design. It should communicate our premier status, but grab attention as innovative. DESIGN SHOULD BE ELEGANT AND NOT TOO BUSY.
Nice to have
• Repeating pattern, multi-color, something creative...
Should not have
• Anything that looks too playful or that we are not serious professionals. It should also not be too boring or conservative.

```html
<!DOCTYPE html>
<html lang="en">
<head>
<meta charset="utf-8">
<title>K4 Business Card</title>
<link href="https://fonts.googleapis.com/css2?family=Poppins:wght@400;500;700;800&display=swap" rel="stylesheet">
<style>
  :root {
    --stage: #1c1c1e;
    --card-front: #1a1a1a;
    --card-front-edge: #262626;
    --card-back: #232323;
    --ink-light: #f4f4f4;
    --ink-muted: #cfcfcf;
    --rule: #bdbdbd;
    --emboss: #2b2b2b;
    --emboss-light: #3a3a3a;
    --band: #2e2e2e;
    --band-ink: #1b1b1b;
  }
  * { box-sizing: border-box; margin: 0; padding: 0; }
  html, body {
    width: 1200px; height: 801px; overflow: hidden;
    background: var(--stage);
    font-family: "Poppins", sans-serif;
  }
  .stage {
    position: relative; width: 1200px; height: 801px;
    display: flex; align-items: center; justify-content: center; gap: 40px;
  }
  .card {
    position: relative; width: 520px; height: 300px;
    border-radius: 18px; overflow: hidden;
    box-shadow: 0 18px 40px rgba(0,0,0,.55);
  }
  /* Front */
  .card-front {
    background: linear-gradient(135deg, var(--card-front-edge), var(--card-front) 60%);
    color: var(--ink-light);
  }
  .front-logo {
    position: absolute; top: 34px; right: 70px;
    font-weight: 800; font-size: 64px; line-height: 1; letter-spacing: 1px;
    color: var(--ink-light);
  }
  .front-rule {
    position: absolute; left: 36px; right: 36px; top: 150px;
    height: 1px; background: var(--rule);
  }
  .address {
    position: absolute; right: 36px; top: 160px; text-align: right;
    font-size: 11px; line-height: 1.45; color: var(--ink-muted);
  }
  .identity { position: absolute; left: 36px; bottom: 34px; width: 300px; }
  .name { font-weight: 700; font-size: 21px; letter-spacing: .5px; line-height: 1.1; }
  .role { font-size: 12px; margin-top: 3px; color: var(--ink-muted); }
  .creds { font-size: 9.5px; font-weight: 500; color: var(--ink-muted); }
  .identity-rule { height: 1px; width: 150px; background: var(--rule); margin: 9px 0 8px; }
  .contact-row { display: flex; gap: 18px; }
  .contact {
    display: flex; align-items: center; gap: 6px;
    font-size: 11px; line-height: 1.6; color: var(--ink-light);
  }
  .contact svg { width: 11px; height: 11px; flex: none; }
  /* Back */
  .card-back {
    background: linear-gradient(160deg, #2a2a2a, var(--card-back) 55%, #1d1d1d);
  }
  .back-logo {
    position: absolute; left: 0; right: 0; top: 30px; text-align: center;
    font-weight: 800; font-size: 150px; line-height: 1; color: var(--emboss);
    text-shadow: 1px 1px 0 var(--emboss-light), -1px -1px 0 #161616;
  }
  .tagline-band {
    position: absolute; left: 0; right: 0; top: 206px; height: 44px;
    background: var(--band);
    display: flex; align-items: center; justify-content: center;
  }
  .tagline {
    font-weight: 800; font-size: 24px; letter-spacing: 1px;
    color: var(--band-ink);
  }
</style>
</head>
<body>
<main class="stage">
  <section class="card card-front" aria-label="Card front">
    <div class="front-logo">K4</div>
    <div class="front-rule"></div>
    <p class="address">2307 Larkmoor, Irvine<br>CA 92741</p>
    <div class="identity">
      <h1 class="name">NOAH PELLINGER</h1>
      <p class="role">CEO</p>
      <p class="creds">PE, HFDP, LEED AP</p>
      <div class="identity-rule"></div>
      <div class="contact-row">
        <p class="contact">
          <svg viewBox="0 0 12 12"><rect width="12" height="12" rx="2" fill="#f4f4f4"/><path d="M3.4 2.8l1.4 1.5-.7.9a5 5 0 0 0 2.7 2.7l.9-.7 1.5 1.4-.9 1a6.3 6.3 0 0 1-5.9-5.9z" fill="#1a1a1a"/></svg>
          +1 949 555 0142
        </p>
        <p class="contact">
          <svg viewBox="0 0 12 12"><rect width="12" height="12" rx="2" fill="#f4f4f4"/><circle cx="6" cy="6" r="3.4" fill="none" stroke="#1a1a1a" stroke-width="1"/><path d="M2.6 6h6.8M6 2.6c-1.6 2-1.6 4.8 0 6.8M6 2.6c1.6 2 1.6 4.8 0 6.8" fill="none" stroke="#1a1a1a" stroke-width=".8"/></svg>
          k4eng.com
        </p>
      </div>
      <p class="contact">
        <svg viewBox="0 0 12 12"><rect width="12" height="12" rx="2" fill="#f4f4f4"/><rect x="2.5" y="3.5" width="7" height="5" fill="none" stroke="#1a1a1a" stroke-width="1"/><path d="M2.5 3.5L6 6.3 9.5 3.5" fill="none" stroke="#1a1a1a" stroke-width="1"/></svg>
        noah.pellinger@k4eng.com
      </p>
    </div>
  </section>

  <section class="card card-back" aria-label="Card back">
    <div class="back-logo">K4</div>
    <div class="tagline-band">
      <p class="tagline">ENGINEERING YOUR FUTURE</p>
    </div>
  </section>
</main>
</body>
</html>
```